K&T Fixit and Rebuild general contracting business card design

I already have a logo that I want to use and I need a card that uses that logo and color scheme on the front with the address phone numbers and email and on the back a place for technicians to write in their name and phone number when they hand it out. It will need the License number of License #KTFXTRB318QN.
It should say General Contractor under the company name. The address is
4417 NE 3rd Ave, Ste D246
Vancouver, WA 98612
www.kandtfixitandrebuild.example
office@kandtfixitandrebuild.example
360-555-0182 is the telephone number
360-555-0149 is the fax number

Target Market(s)

Homeowners needing remodel work or repairs in their home.

Industry/Entity Type

Construction

Contact Information for Business Card

Business name, address, phone number, license number, fax number, email, and website on the front and a place to fill in technician's name and number

Font styles to use
Serif

Requirements
Must have
• Business name, address, phone number, license number, fax number, email, and website on the front and a place to fill in technician's name and number
Nice to have
• I uploaded an example of a front that is good.
Should not have
• Froo froo or extra embellishments.

```html
<!DOCTYPE html>
<html lang="en">
<head>
<meta charset="utf-8">
<title>K&amp;T Fixit and Rebuild — Business Card</title>
<link rel="stylesheet" href="https://fonts.googleapis.com/css2?family=Arimo:wght@400;700&display=swap">
<style>
  :root {
    --stage: #2e2e2e;
    --wood-light: #8a6e30;
    --wood-mid: #735a24;
    --wood-dark: #54421a;
    --ink-white: #ffffff;
    --copper: #b8623a;
    --ink-dark: #1e1e1e;
    --rule: #8a8a8a;
    --paper: #ffffff;
  }
  * { box-sizing: border-box; margin: 0; padding: 0; }
  html, body {
    width: 1200px;
    height: 866px;
    overflow: hidden;
    background: var(--stage);
    font-family: "Arimo", Arial, sans-serif;
  }
  .sheet {
    width: 1200px;
    height: 866px;
    display: flex;
    flex-direction: column;
    align-items: center;
    justify-content: center;
    gap: 40px;
  }
  .card {
    position: relative;
    width: 640px;
    height: 366px;
    overflow: hidden;
    box-shadow: 0 10px 24px rgba(0,0,0,0.55);
  }

  /* Front */
  .card-front { color: var(--ink-white); }
  .workbench-photo {
    position: absolute;
    inset: 0;
    background:
      radial-gradient(ellipse at 50% 45%, var(--wood-light) 0%, var(--wood-mid) 55%, var(--wood-dark) 100%);
  }
  .front-content {
    position: absolute;
    left: 200px;
    top: 58px;
    width: 380px;
  }
  .company-name {
    font-weight: 700;
    font-size: 34px;
    line-height: 1.05;
    letter-spacing: 0.5px;
    margin-bottom: 6px;
  }
  .license {
    font-size: 13px;
    margin-bottom: 22px;
  }
  .contact-list {
    list-style: none;
    font-size: 16px;
    line-height: 1.4;
  }
  .contact-list .label { font-weight: 700; }
  .contact-list .gap { margin-top: 8px; }

  /* Back */
  .card-back { background: var(--paper); color: var(--ink-dark); }
  .back-brand {
    position: absolute;
    left: 250px;
    top: 70px;
    width: 340px;
    color: var(--copper);
  }
  .back-brand .company-name { font-size: 32px; margin-bottom: 10px; }
  .tagline {
    font-size: 17px;
    letter-spacing: 1.5px;
    text-transform: uppercase;
  }
  .write-in {
    position: absolute;
    left: 70px;
    top: 222px;
    width: 480px;
    font-size: 19px;
  }
  .write-in-row {
    display: flex;
    align-items: flex-end;
    gap: 12px;
    height: 38px;
  }
  .write-in-row .field-label { width: 84px; }
  .write-in-row .field-line {
    flex: 1;
    border-bottom: 1px solid var(--rule);
    height: 22px;
  }
</style>
</head>
<body>
<main class="sheet">
  <section class="card card-front" aria-label="Card front">
    <div class="workbench-photo" role="img" aria-label="Photo of a wooden workbench with a hammer, pliers, wrenches, a level, tape measure and a drill bit"></div>
    <div class="front-content">
      <h1 class="company-name">K&amp;T Fixit and Rebuild</h1>
      <p class="license">License #KTFXTRB318QN</p>
      <ul class="contact-list">
        <li><span class="label">P:</span> 360-555-0182</li>
        <li><span class="label">F:</span> 360-555-0149</li>
        <li class="gap">office@kandtfixitandrebuild.example</li>
        <li>www.kandtfixitandrebuild.example</li>
        <li class="gap">4417 NE 3rd Ave, Ste D246</li>
        <li>Vancouver, WA 98612</li>
      </ul>
    </div>
  </section>

  <section class="card card-back" aria-label="Card back">
    <div class="back-brand">
      <h2 class="company-name">K&amp;T Fixit and Rebuild</h2>
      <p class="tagline">General Contractor</p>
    </div>
    <div class="write-in">
      <div class="write-in-row"><span class="field-label">Name:</span><span class="field-line"></span></div>
      <div class="write-in-row"><span class="field-label">Contact:</span><span class="field-line"></span></div>
    </div>
  </section>
</main>
</body>
</html>
```